Gale Sentry - WEBSITE Contest - 4-5 pages coding - Strong, simple clean WORDPRESS

Hello,
The inspiriation website is www.brixhalo.com
Please look at this site because I want to copy that.
I have changed the order a little bit so please look at my order of the site elements.
I will supply text, please just use lorem ipsum for now.
PLEASE LOOK AT THE BRIX HALO WEBSITE AND MAKE A COPY OF THAT.
PPlease look at that site and see the different features it has and make that.
We will need this main page and then:
-About Us page
-Contact Us page
-Request a quote page / fillable form
-1 product/service page
Thank you,
Trevor
/////////////////////////////
Website design for Gale Sentry.
Please design with simple, easy to read fonts. Customers are older and need strong, bold easy to read.
galesentry-demo.com
Tel (555) 318-4072
trevor@galesentry-demo.com
The problem is that all roofing vents leak. We have a product that goes into the vent that stops the roof from leaking.
Your beautiful Florida home is unprotected!
All roof vents leak!
Winds over 30 MPH push rainwater INTO your home through the rooftop vents! The result is water damage that can cost thousands of dollars to repair and remediate!
The GALE SENTRY is a powerful roof vent protection system, engineered to block wind driven rains from entering your home's roof vents.
The Gale Sentry is made to withstand extreme conditions. Featuring IMPACT hurricane screening and powerful steel construction.
Professional installation is permanent and concealed and is accomplished via the roof top.
Get protected for all the storms ahead! Get the Gale Sentry!
www.galesentry-demo.com
Call Now: 555 318-4072
Updates
Hello to all designers - please add a "SERVICE AREA MAP" widget to the designs. Thank you.
Target Market(s)
The target customer is a affluent, older couple 50-60 years old. Homeowner. middle class to upper class adults / ages 50-60 years old (older but not VERY old)
Industry/Entity Type
roofing and construction
Coding
Coded - Design and coding required
Number of Pages Required
4 page
Colors
Designer to choose colors to be used in the design.
Requirements
Must have
- Great landing page, about us page, product page, contact us page, request quote form / Strong, simple clean
Nice to have
- feelings: professional / strong / reliable / safety / shelter / security / future stability/ calm / security
Should not have
- stress / fear feeling - this product will remove fear and stress of damages from storms

```html
<!DOCTYPE html>
<html lang="en">
<head>
<meta charset="utf-8">
<title>About Us – Gale Sentry</title>
<link rel="stylesheet" href="https://fonts.googleapis.com/css2?family=Montserrat:wght@400;500;700;800;900&family=Poppins:wght@300;400;600;700&family=Playfair+Display:ital,wght@1,500&display=swap">
<style>
:root{
  --ink:#0c0f13;
  --navy-top:#0a0e13;
  --sky:#8fc3ef;
  --sky-mid:#4f7fa8;
  --accent:#4aa3e0;
  --brand-blue:#1f6fb8;
  --white:#ffffff;
  --text:#222831;
  --card-edge:#9fb3c7;
  --footer:#161819;
  --footer-bar:#0d0e0f;
}
*{margin:0;padding:0;box-sizing:border-box}
html,body{width:1200px;height:2455px;overflow:hidden}
body{font-family:'Montserrat',sans-serif;color:var(--text);background:var(--ink);position:relative}

.hero{position:absolute;left:0;top:0;width:1200px;height:441px;
  background:linear-gradient(180deg,#4d6474 0%,#5b6c74 35%,#6b5748 62%,#4a3a2e 100%)}
.hero-shade{position:absolute;inset:0;background:linear-gradient(180deg,rgba(40,55,70,.55),rgba(30,30,30,.25))}
.site-header{position:absolute;left:0;top:0;width:1200px;height:95px;background:rgba(50,68,84,.82);border-bottom:1px solid rgba(255,255,255,.08)}
.brand{position:absolute;left:80px;top:22px;display:flex;align-items:center;gap:14px;color:var(--white);font-family:'Montserrat',sans-serif;font-weight:700;font-size:30px;letter-spacing:1px}
.brand-dot{width:50px;height:50px;border-radius:50%;background:var(--white)}
.nav{position:absolute;top:36px;left:427px;display:flex;font-size:13px;color:var(--white);font-weight:500}
.nav a{color:inherit;text-decoration:none;position:absolute;white-space:nowrap}
.nav a.active::after{content:"";position:absolute;left:0;right:0;top:21px;height:2px;background:var(--accent)}
.nav-divider{position:absolute;left:968px;top:34px;width:1px;height:22px;background:rgba(255,255,255,.4)}
.phone{position:absolute;left:997px;top:33px;display:flex;align-items:center;gap:8px;color:var(--white);font-weight:700;font-size:16px}
.hero-title{position:absolute;left:0;top:202px;width:1200px;text-align:center;color:var(--white);font-weight:700;font-size:34px;line-height:45px}
.hero-rule{position:absolute;left:512px;top:314px;width:193px;height:2px;background:rgba(255,255,255,.85)}

.story{position:absolute;left:0;top:441px;width:1200px;height:1200px;
  background:linear-gradient(180deg,var(--navy-top) 0%,#1a2a3a 18%,var(--sky-mid) 45%,#7fb3e2 70%,var(--sky) 100%)}
.photo{position:absolute}
.about-photo{left:130px;top:73px;width:546px;height:417px;background:linear-gradient(165deg,#6fa6d8 0%,#9eb8b8 14%,#7b7d80 30%,#5d5b5a 60%,#7a6a60 100%)}
.about-accent{position:absolute;left:891px;top:324px;width:198px;height:116px;background:var(--accent)}
.about-card{position:absolute;left:600px;top:133px;width:480px;height:296px;background:var(--white);padding:72px 26px 0 42px}
.eyebrow{font-size:12px;letter-spacing:4px;color:#333;font-weight:500}
.about-card h1{font-family:'Montserrat',sans-serif;font-weight:900;font-size:42px;color:#050608;margin-top:4px;line-height:48px}
.about-card h1 em{font-family:'Playfair Display',serif;font-style:italic;font-weight:500;color:var(--brand-blue);margin-left:10px}
.about-card p{margin-top:18px;font-size:16.5px;line-height:24px;color:#1e2329}

.step-photo{position:absolute;width:311px;height:241px;clip-path:polygon(0 0,100% 0,100% 85%,0 100%)}
.step-1{left:117px;top:553px;background:linear-gradient(160deg,#b9c4cc 0%,#4f6d85 40%,#e6ecef 55%,#2f5170 100%)}
.step-2{left:447px;top:553px;background:linear-gradient(180deg,#a9c5d9 0%,#eef2f4 35%,#cfd6dc 70%,#9aa6b0 100%)}
.step-3{left:779px;top:553px;background:linear-gradient(170deg,#6d7f64 0%,#bfc3c4 40%,#8c9093 75%,#556b4a 100%)}
.step-card{position:absolute;width:287px;height:262px;background:var(--card-edge);clip-path:polygon(0 6%,100% 0,100% 100%,0 100%)}
.step-card-inner{position:absolute;inset:3px;background:var(--white);clip-path:polygon(0 6%,100% 0,100% 100%,0 100%);text-align:center;padding:34px 16px 0}
.step-icon{width:44px;height:44px;border:2px solid var(--brand-blue);border-radius:50%;margin:0 auto 14px}
.step-card p{font-size:15.5px;line-height:23px;color:#1e2329}
.c1{left:130px;top:732px}.c2{left:460px;top:732px}.c3{left:792px;top:732px}

.tagline{position:absolute;left:0;top:1085px;width:1200px;text-align:center;color:var(--white);font-family:'Poppins',sans-serif;font-size:37px;line-height:43px}
.tagline strong{font-weight:700;display:block}
.tagline span{font-weight:300;display:block}

.neighborhood{position:absolute;left:0;top:1625px;width:1200px;height:365px;
  background:linear-gradient(180deg,#52684a 0%,#6d6a58 18%,#3e6b84 34%,#b06a48 52%,#c27a56 75%,#8e5a40 100%)}

.site-footer{position:absolute;left:0;top:1990px;width:1200px;height:390px;background:linear-gradient(180deg,#121314,var(--footer) 60%,#2a2c2e);color:var(--white);font-family:'Poppins',sans-serif}
.footer-col h3{font-size:19px;font-weight:600}
.footer-col h3::after{content:"";display:block;width:22px;height:2px;background:var(--white);margin-top:10px}
.contact-col{position:absolute;left:148px;top:92px}
.contact-list{list-style:none;margin-top:14px;font-size:14px}
.contact-list li{display:flex;gap:10px;align-items:flex-start;height:41px}
.contact-list svg{flex:none;margin-top:2px}
.footer-brand{position:absolute;left:485px;top:90px;width:245px;text-align:center}
.footer-brand .brand-dot{width:80px;height:80px;margin:0 auto 22px}
.footer-brand div{font-family:'Montserrat',sans-serif;font-weight:700;font-size:34px;letter-spacing:1px}
.company-col{position:absolute;left:863px;top:92px}
.company-col ul{list-style:none;margin-top:10px;font-size:14px;line-height:28.5px}
.footer-bar{position:absolute;left:0;top:2380px;width:1200px;height:75px;background:var(--footer-bar);color:var(--white);font-family:'Poppins',sans-serif;font-size:13px}
.copyright{position:absolute;left:148px;top:26px}
.copyright u{text-decoration:underline}
.social{position:absolute;left:928px;top:21px;display:flex;gap:5px}
.social i{width:27px;height:27px;border-radius:50%;background:var(--white)}
</style>
</head>
<body>

<section class="hero" role="img" aria-label="Aerial photo of tiled Florida rooftops">
  <div class="hero-shade"></div>
</section>

<header class="site-header">
  <div class="brand"><span class="brand-dot"></span>GALE SENTRY</div>
  <nav class="nav">
    <a class="active" style="left:0">About Us</a>
    <a style="left:105px">Products</a>
    <a style="left:208px">Service Areas</a>
    <a style="left:345px">Blogs</a>
    <a style="left:425px">Contact Us</a>
  </nav>
  <span class="nav-divider"></span>
  <div class="phone">
    <svg width="20" height="20" viewBox="0 0 24 24" fill="none" stroke="#fff" stroke-width="1.6"><path d="M5 3h4l2 5-2.5 1.5a11 11 0 0 0 6 6L16 13l5 2v4a2 2 0 0 1-2 2A16 16 0 0 1 3 5a2 2 0 0 1 2-2z"/></svg>
    555 318-4072
  </div>
</header>

<h2 class="hero-title">We go sick of seeing water intrusion and damage<br>And decided to do something about it</h2>
<span class="hero-rule"></span>

<main class="story">
  <div class="photo about-photo" role="img" aria-label="Tile roof with vent covers overlooking a lake"></div>
  <div class="about-accent"></div>
  <div class="about-card">
    <div class="eyebrow">WHO WE ARE</div>
    <h1>About<em>Us</em></h1>
    <p>As a driven team of master building inspectors and engineers, it was time to put a stop roof vent leaks.</p>
  </div>

  <div class="step-photo step-1" role="img" aria-label="Satellite view of a hurricane over the coast"></div>
  <div class="step-photo step-2" role="img" aria-label="White metal roof with impact windows"></div>
  <div class="step-photo step-3" role="img" aria-label="Steel roof vent protection unit"></div>

  <div class="step-card c1"><div class="step-card-inner"><div class="step-icon"></div>
    <p>Again and again we saw anxious homeowners, worried the next storm would bring more water intrusion and damage.</p></div></div>
  <div class="step-card c2"><div class="step-card-inner"><div class="step-icon"></div>
    <p>Most homes had impact windows and shutters. So why were the roof vents not protected? Why were they wide open to water intrusion?</p></div></div>
  <div class="step-card c3"><div class="step-card-inner"><div class="step-icon"></div>
    <p>And that's why we built the Gale Sentry system, to help homeowners completely stop roof vent water intrusion.</p></div></div>

  <h2 class="tagline"><strong>To bring safety and comfort back</strong><span>for all the storms ahead.</span></h2>
</main>

<section class="neighborhood" role="img" aria-label="Terracotta roof ridge above a lakeside neighborhood"></section>

<footer class="site-footer">
  <div class="footer-col contact-col">
    <h3>Contact Us</h3>
    <ul class="contact-list">
      <li><svg width="18" height="18" viewBox="0 0 24 24" fill="#fff"><path d="M5 3h4l2 5-2.5 1.5a11 11 0 0 0 6 6L16 13l5 2v4a2 2 0 0 1-2 2A16 16 0 0 1 3 5a2 2 0 0 1 2-2z"/></svg>Call Now: 555 318-4072</li>
      <li><svg width="18" height="18" viewBox="0 0 24 24" fill="#fff"><path d="M2 5h20v14H2z"/><path d="M2 5l10 8 10-8" stroke="#161819" stroke-width="2" fill="none"/></svg>trevor@galesentry-demo.com</li>
      <li><svg width="18" height="18" viewBox="0 0 24 24" fill="none" stroke="#fff" stroke-width="2"><circle cx="12" cy="12" r="10"/><path d="M2 12h20M12 2c3 3 3 17 0 20M12 2c-3 3-3 17 0 20"/></svg>www.galesentry-demo.com</li>
      <li><svg width="18" height="18" viewBox="0 0 24 24" fill="#fff"><path d="M12 2a7 7 0 0 0-7 7c0 5 7 13 7 13s7-8 7-13a7 7 0 0 0-7-7zm0 9.5A2.5 2.5 0 1 1 12 6a2.5 2.5 0 0 1 0 5.5z"/></svg>1420 Palmetto Row<br>Coral Bay, FL 34000</li>
    </ul>
  </div>
  <div class="footer-brand"><span class="brand-dot"></span><div>GALE SENTRY</div></div>
  <div class="footer-col company-col">
    <h3>Company</h3>
    <ul><li>Home</li><li>About Us</li><li>Products</li><li>Contact Us</li></ul>
  </div>
</footer>

<div class="footer-bar">
  <p class="copyright">Copyright © 2023 <u>Gale Sentry</u>. All Rights Reserved</p>
  <div class="social"><i></i><i></i><i></i><i></i></div>
</div>

</body>
</html>
```